Packaging design for handmade soap

We are looking for a packaging design for a brand new product line: handmade soaps, called BRIVO

We are looking for a design of an outer box together with the logo. We need the design for a 90x65x30mm box (see attached). We trying to get a high-end product preferable with vintage elements (but we don't want a shiny box, it will be finished with matte lacque, however logo or other certain elements could be shiny).

The design should reflect the fact that we have a handmade, all natural soap.

I uploaded a couple of packaging examples I like.

UPDATE 1: It also should have a title, which describes the product more accurate, like "Natural Soap with Seabuckthorn and Olive oil"

UPDATE 2: I would remove the expression "high-end" from the description if high end would mean a lot of flowers in the background. I would like if you would insist about the ideea of "natural" in your works

UPDATE 3: Prefered colors green and brown (which brings the ideea of nature, natural)

Target Market(s)

Women 20-45 years with above average income

Industry/Entity Type

Cosmetics

Font styles to use
Serif

Colors
9bcb3c
acd036
cadf82
f78f20
ffc214
f37122
fbed22
fece3e
faa54b

Requirements
Must have
• A literal representation of the brand BRIVO (we don't have a logo for it)

```html
<!DOCTYPE html>
<html lang="en">
<head>
<meta charset="utf-8">
<title>BRIVO natural handmade soap – box panels</title>
<link rel="stylesheet" href="https://fonts.googleapis.com/css2?family=Cinzel:wght@600&family=PT+Sans:wght@400&display=swap">
<style>
  :root {
    --page: #f5f1ea;
    --kraft: #e8dcb5;
    --amber: #f5a623;
    --amber-text: #f29a1e;
    --leaf: #1f7a33;
    --sky: #a9cfe2;
    --lime: #c3dc7e;
    --sage: #9fb8a8;
    --mist: #eef1e6;
  }
  html, body {
    margin: 0;
    width: 1200px;
    height: 1200px;
    overflow: hidden;
    background: var(--page);
  }
  .box-net {
    position: absolute;
    left: 80px;
    top: 188px;
    width: 1040px;
    height: 824px;
    overflow: visible;
  }
  .panel { fill: var(--kraft); stroke: var(--amber); stroke-width: 1; }
  .band-edge { stroke: var(--amber); stroke-width: 1.5; }
  .label-shape { fill: var(--kraft); stroke: var(--amber); stroke-width: 4; }
  .label-inner-line { fill: none; stroke: var(--amber); stroke-width: 1.5; }
  .brand-name {
    font-family: "Cinzel", serif;
    font-weight: 600;
    fill: var(--amber-text);
    letter-spacing: 4px;
  }
  .brand-rule { stroke: var(--leaf); stroke-width: 3; }
  .tagline, .net-weight {
    font-family: "PT Sans", sans-serif;
    font-weight: 400;
    fill: var(--leaf);
  }
  .tagline { font-size: 23px; }
  .net-weight { font-size: 17px; }
</style>
</head>
<body>
  <svg class="box-net" viewBox="0 0 1196 947" xmlns="http://www.w3.org/2000/svg">
    <defs>
      <linearGradient id="pattern-tones" x1="0" y1="0" x2="1" y2="1">
        <stop offset="0" stop-color="#b9d7e6"/>
        <stop offset="0.35" stop-color="#d3e3a4"/>
        <stop offset="0.65" stop-color="#b6c9bc"/>
        <stop offset="1" stop-color="#c6dde9"/>
      </linearGradient>
    </defs>

    <!-- top panel -->
    <g class="top-panel">
      <rect class="panel" x="0" y="0" width="897" height="299"/>
      <text class="brand-name" x="448" y="180" font-size="80" text-anchor="middle">BRIVO</text>
    </g>

    <!-- side panel -->
    <g class="side-panel">
      <rect class="panel" x="897" y="299" width="299" height="648"/>
      <text class="brand-name" x="0" y="0" font-size="80" text-anchor="middle"
            transform="translate(1046 623) rotate(90) translate(0 28)">BRIVO</text>
    </g>

    <!-- front panel -->
    <g class="front-panel" transform="translate(0 299)">
      <rect class="panel" x="0" y="0" width="897" height="648"/>
      <g role="img" aria-label="Decorative pattern of overlapping blue, green and sand coloured organic blobs with small dots">
        <rect x="0" y="0" width="356" height="648" fill="url(#pattern-tones)"/>
      </g>
      <g role="img" aria-label="Decorative pattern of overlapping blue, green and sand coloured organic blobs with small dots">
        <rect x="540" y="0" width="357" height="648" fill="url(#pattern-tones)"/>
      </g>
      <line class="band-edge" x1="356" y1="0" x2="356" y2="648"/>
      <line class="band-edge" x1="540" y1="0" x2="540" y2="648"/>

      <path class="label-shape"
        d="M 235 150 C 240 110, 330 105, 360 125 C 400 140, 510 140, 550 125 C 580 105, 670 110, 675 150 C 680 200, 700 230, 740 260 C 770 290, 770 370, 735 395 C 700 420, 680 450, 675 500 C 670 540, 580 545, 550 525 C 510 510, 400 510, 360 525 C 330 545, 240 540, 235 500 C 230 450, 210 420, 175 395 C 140 370, 140 290, 170 260 C 210 230, 230 200, 235 150 Z"/>
      <path class="label-inner-line"
        transform="translate(455 325) scale(0.92) translate(-455 -325)"
        d="M 235 150 C 240 110, 330 105, 360 125 C 400 140, 510 140, 550 125 C 580 105, 670 110, 675 150 C 680 200, 700 230, 740 260 C 770 290, 770 370, 735 395 C 700 420, 680 450, 675 500 C 670 540, 580 545, 550 525 C 510 510, 400 510, 360 525 C 330 545, 240 540, 235 500 C 230 450, 210 420, 175 395 C 140 370, 140 290, 170 260 C 210 230, 230 200, 235 150 Z"/>

      <text class="brand-name" x="463" y="280" font-size="84" text-anchor="middle">BRIVO</text>
      <line class="brand-rule" x1="330" y1="307" x2="603" y2="307"/>
      <text class="tagline" x="464" y="346" text-anchor="middle">natural handmade soap</text>
      <text class="net-weight" x="460" y="454" text-anchor="middle">100gm/3.53oz</text>
    </g>
  </svg>
</body>
</html>
```